Redesign my business cards

I would like pretty much all the same information as my current business cards but redesigned to stand out more and be more unique photo uploaded to show my current business cards don’t mind if you want to remove or replace I for on the back

```html
<!DOCTYPE html>
<html lang="en">
<head>
<meta charset="UTF-8">
<title>Brightmere Detailing – Business Card</title>
<link href="https://fonts.googleapis.com/css2?family=Arimo:ital,wght@0,400;0,700;1,700&display=swap" rel="stylesheet">
<style>
  :root{
    --page:#2b2724;
    --front-centre:#44bcd9;
    --front-edge:#3070c9;
    --navy:#07293b;
    --navy-soft:#0d3a52;
    --accent:#8a2fe0;
    --role:#e0263c;
    --light:#ffffff;
    --head:#4a93e4;
    --body-text:#dbe6ec;
    --leader:rgba(255,255,255,.25);
  }
  *{box-sizing:border-box;margin:0;padding:0}
  html,body{width:1200px;height:716px;overflow:hidden;background:var(--page)}
  body{font-family:"Arimo",Arial,sans-serif;position:relative}

  .card{position:absolute;top:198px;width:560px;height:320px;overflow:hidden;box-shadow:0 10px 30px rgba(0,0,0,.5)}
  .card--front{left:26px;background:radial-gradient(ellipse at 35% 45%,var(--front-centre) 0%,var(--front-edge) 80%)}
  .card--back{left:614px;background:var(--navy);padding:26px 30px}

  /* front */
  .brand-panel{position:absolute;top:0;right:0;width:230px;height:100%;background:var(--navy);clip-path:polygon(70px 0,100% 0,100% 100%,0 100%)}
  .brand{position:absolute;right:28px;top:50%;transform:translateY(-50%);display:flex;flex-direction:column;align-items:center;gap:12px;width:140px;text-align:center}
  .brand__dot{width:46px;height:46px;border-radius:50%;background:var(--accent)}
  .brand__name{font-size:17px;font-weight:700;line-height:1.2;color:var(--light);letter-spacing:.5px}

  .owner{position:absolute;left:36px;top:62px}
  .owner__name{font-size:30px;font-weight:700;color:var(--light);letter-spacing:1px}
  .owner__role{font-size:13px;font-weight:700;color:var(--navy);letter-spacing:2px;text-transform:uppercase;margin-top:6px}
  .owner__bar{width:56px;height:4px;background:var(--accent);margin-top:14px}

  .contact{position:absolute;left:36px;bottom:40px;display:flex;flex-direction:column;gap:10px}
  .contact__item{display:flex;align-items:center;gap:10px;font-size:14px;color:var(--light)}
  .contact__icon{width:24px;height:24px;border-radius:50%;background:var(--navy);display:flex;align-items:center;justify-content:center}
  .contact__icon svg{width:12px;height:12px}

  /* back */
  .menu__heading{font-size:12px;font-weight:700;letter-spacing:3px;text-transform:uppercase;color:var(--accent);margin-bottom:16px}
  .service{margin-bottom:16px}
  .service__row{display:flex;align-items:baseline;gap:10px}
  .service__title{font-size:16px;font-weight:700;font-style:italic;color:var(--head);white-space:nowrap}
  .service__leader{flex:1;border-bottom:1px dotted var(--leader);transform:translateY(-4px)}
  .service__price{font-size:16px;font-weight:700;color:var(--light)}
  .service__text{font-size:12px;line-height:1.4;color:var(--body-text);margin-top:4px}
  .back-bar{position:absolute;left:0;bottom:0;width:100%;height:6px;background:var(--accent)}
</style>
</head>
<body>
  <section class="card card--front">
    <div class="owner">
      <p class="owner__name">JORDAN KELLS</p>
      <p class="owner__role">Owner Operator</p>
      <div class="owner__bar"></div>
    </div>
    <div class="contact">
      <p class="contact__item">
        <span class="contact__icon"><svg viewBox="0 0 24 24"><path fill="#ffffff" d="M6.6 10.8a15 15 0 0 0 6.6 6.6l2.2-2.2c.3-.3.7-.4 1-.2 1.1.4 2.3.6 3.6.6.6 0 1 .4 1 1V20c0 .6-.4 1-1 1A17 17 0 0 1 3 4c0-.6.4-1 1-1h3.5c.6 0 1 .4 1 1 0 1.3.2 2.5.6 3.6.1.3 0 .7-.2 1z"/></svg></span>
        0412555019
      </p>
      <p class="contact__item">
        <span class="contact__icon"><svg viewBox="0 0 13 10"><rect width="13" height="10" rx="1" fill="#ffffff"/><path d="M0.5 0.8 6.5 5.5 12.5 0.8" stroke="#07293b" stroke-width="1.2" fill="none"/></svg></span>
        brightmeredetailing@example.com
      </p>
    </div>
    <div class="brand-panel"></div>
    <div class="brand">
      <span class="brand__dot"></span>
      <span class="brand__name">Brightmere Detailing</span>
    </div>
  </section>

  <section class="card card--back">
    <p class="menu__heading">Detailing Packages</p>
    <div class="service">
      <div class="service__row"><h2 class="service__title">Interior Detail</h2><span class="service__leader"></span><span class="service__price">$150</span></div>
      <p class="service__text">Vacuum &amp; deep clean of carpets &amp; upholstery or leather treatment, interior trim clean &amp; condition, window polish &amp; treatment, steam clean and stain removal</p>
    </div>
    <div class="service">
      <div class="service__row"><h2 class="service__title">Exterior Detail</h2><span class="service__leader"></span><span class="service__price">$250</span></div>
      <p class="service__text">Extreme wash &amp; polish, exterior trim reviver &amp; protector, window polish &amp; treatment, tyre dressing, engine bay cleaned</p>
    </div>
    <div class="service">
      <div class="service__row"><h2 class="service__title">Full Extreme Detail</h2><span class="service__leader"></span><span class="service__price">$350</span></div>
      <p class="service__text">Everything above: extreme wash &amp; polish, tyre dressing, engine bay cleaned, deep clean of carpets &amp; upholstery or leather treatment, interior &amp; exterior trim reviver &amp; protector, window polish</p>
    </div>
    <div class="back-bar"></div>
  </section>
</body>
</html>
```